Business Card Design Project

We would need a business name card for our online website business, http://www.brindle.com.sg/. We would need to include our website on the name card as well.

Target Market(s)

Adults and kids in Singapore, mainly expatriates

Industry/Entity Type

Business

Font styles to use
Sans Serif

Colors

Designer to choose colors to be used in the design.

Requirements
Must have
• Must include our "vorn" logo and we would like our name card to be printed on light craft paper material

```html
<!DOCTYPE html>
<html lang="en">
<head>
<meta charset="utf-8">
<title>Vorn Shop – Business Card</title>
<link rel="stylesheet" href="https://fonts.googleapis.com/css2?family=Nunito+Sans:wght@400;600;700;800&display=swap">
<style>
  :root {
    --backdrop: #e7e4df;
    --kraft: #c99a5e;
    --kraft-dark: #b8884f;
    --navy: #1b2a6d;
    --roundel-red: #e3344a;
    --ink: #141414;
    --band-text: #c99a5e;
  }
  * { margin: 0; padding: 0; box-sizing: border-box; }
  html, body {
    width: 1200px; height: 1000px; overflow: hidden;
    background: var(--backdrop);
    font-family: "Nunito Sans", Arial, sans-serif;
  }
  .canvas { position: relative; width: 1200px; height: 1000px; }
  .card {
    position: absolute; left: 265px; width: 667px; height: 397px;
    background: var(--kraft);
    box-shadow: 0 3px 10px rgba(0,0,0,0.18);
    overflow: hidden;
  }
  .card--front { top: 73px; }
  .card--back { top: 532px; }

  .brand-mark {
    position: absolute; inset: 0;
    display: flex; align-items: center; justify-content: center; gap: 22px;
  }
  .brand-mark__name {
    font-weight: 800; font-size: 96px; letter-spacing: 4px;
    color: var(--navy); line-height: 1;
  }
  .brand-mark__dot {
    width: 56px; height: 56px; border-radius: 50%;
    background: var(--roundel-red);
  }

  .name-band {
    position: absolute; left: 0; right: 0; top: 76px; height: 57px;
    background: var(--navy);
    display: flex; align-items: center; gap: 14px; padding-left: 32px;
  }
  .name-band__title {
    font-weight: 700; font-size: 35px; letter-spacing: 1px;
    color: var(--band-text); line-height: 1;
  }
  .name-band__square {
    width: 22px; height: 22px; background: var(--band-text);
  }

  .contact {
    position: absolute; left: 32px; top: 170px;
    color: var(--ink);
  }
  .contact__person { font-size: 22px; font-weight: 400; letter-spacing: 0.5px; margin-bottom: 10px; }
  .contact__line { font-size: 17px; line-height: 22px; }
  .contact__line strong { font-weight: 800; }
  .contact__group { margin-bottom: 14px; }
</style>
</head>
<body>
<main class="canvas">
  <section class="card card--front" aria-label="Card front">
    <div class="brand-mark">
      <span class="brand-mark__name">VORN</span>
      <span class="brand-mark__dot" aria-hidden="true"></span>
    </div>
  </section>

  <section class="card card--back" aria-label="Card back">
    <div class="name-band">
      <span class="name-band__title">VORN SHOP</span>
      <span class="name-band__square" aria-hidden="true"></span>
    </div>
    <div class="contact">
      <p class="contact__person">MAYA TAN</p>
      <div class="contact__group">
        <p class="contact__line">6350 4182</p>
        <p class="contact__line">email@<strong>vorncorp</strong>.com</p>
      </div>
      <div class="contact__group">
        <p class="contact__line">www.<strong>brindle</strong>.com.sg</p>
      </div>
      <div class="contact__group">
        <p class="contact__line">48 Harbour Lane #09-11A</p>
        <p class="contact__line">Singapore 058210</p>
      </div>
    </div>
  </section>
</main>
</body>
</html>
```